Design a New Business Card for Our Company

We are looking for fresh, unique, and a modern business card that reflects our roots as digital marketing agency focused on SEM.

Industry/Entity Type

Marketing

Contact Information for Business Card

looking for very unique out of the box designs. clean and modern that compliments our logo

Requirements
Must have
• colors should match our logo
• Front should have name, address, email, and phone/fax of the person, phone/fax are the same number
• back should have our url

```html
<!DOCTYPE html>
<html lang="en">
<head>
<meta charset="utf-8">
<title>Northvale Studio – Business Card</title>
<link rel="stylesheet" href="https://fonts.googleapis.com/css2?family=Lato:ital,wght@0,400;0,700;0,900;1,700&display=swap">
<style>
  :root {
    --page-bg: #ececec;
    --brand-blue: #5b93d3;
    --brand-grey: #a9a9a9;
    --ink: #333333;
    --ink-soft: #444444;
    --card-light-a: #ffffff;
    --card-light-b: #ececec;
    --card-dark-a: #3a3a3a;
    --card-dark-b: #2a2a2a;
    --white: #ffffff;
  }
  * { margin: 0; padding: 0; box-sizing: border-box; }
  html, body {
    width: 1200px; height: 1195px; overflow: hidden;
    background: var(--page-bg);
    font-family: "Lato", Arial, sans-serif;
  }
  .canvas { position: relative; width: 1200px; height: 1195px; }
  .card {
    position: absolute; left: 290px; width: 620px; height: 372px; overflow: hidden;
  }
  .card--front { top: 162px; }
  .card--back { top: 671px; height: 373px; }
  .card__texture { position: absolute; inset: 0; }
  .card--front .card__texture {
    background: linear-gradient(135deg, var(--card-light-a) 0%, var(--card-light-b) 45%, var(--card-light-a) 70%, var(--card-light-b) 100%);
  }
  .card--back .card__texture {
    background: linear-gradient(135deg, var(--card-dark-a) 0%, var(--card-dark-b) 50%, var(--card-dark-a) 100%);
  }
  .brand {
    position: absolute; left: 0; right: 0; display: flex;
    align-items: center; justify-content: center; gap: 10px;
  }
  .brand__dot { border-radius: 50%; background: var(--brand-blue); flex: none; }
  .brand__name { font-weight: 900; color: var(--brand-grey); letter-spacing: -0.5px; white-space: nowrap; line-height: 1.2; }
  .card--front .brand { top: 64px; }
  .card--front .brand__dot { width: 28px; height: 28px; }
  .card--front .brand__name { font-size: 38px; }
  .card--back .brand { top: 132px; gap: 16px; }
  .card--back .brand__dot { width: 46px; height: 46px; }
  .card--back .brand__name { font-size: 52px; }

  .person { position: absolute; right: 368px; top: 205px; text-align: right; }
  .person__name { font-size: 22px; font-weight: 700; color: var(--brand-blue); line-height: 1.1; }
  .person__role { font-size: 16px; font-weight: 400; color: var(--ink); margin-top: 5px; }
  .divider { position: absolute; left: 288px; top: 178px; width: 3px; height: 104px; background: var(--brand-blue); opacity: .8; }
  .contacts { position: absolute; left: 310px; top: 199px; list-style: none; }
  .contacts__item { display: flex; align-items: center; height: 30px; font-size: 15px; font-weight: 700; color: var(--ink-soft); }
  .contacts__icon { width: 16px; height: 16px; margin-right: 10px; fill: var(--brand-blue); flex: none; }
  .address {
    position: absolute; left: 0; right: 0; top: 340px; text-align: center;
    font-size: 15px; font-weight: 700; color: var(--brand-blue);
  }
  .website {
    position: absolute; left: 0; right: 0; top: 313px; text-align: center;
    font-size: 15px; font-weight: 700; font-style: italic; letter-spacing: 3.2px; color: var(--white);
  }
</style>
</head>
<body>
<main class="canvas">
  <section class="card card--front">
    <div class="card__texture" role="img" aria-label="Soft white low-poly faceted texture"></div>
    <div class="brand">
      <span class="brand__dot"></span>
      <span class="brand__name">Northvale Studio</span>
    </div>
    <div class="person">
      <p class="person__name">Daniel Hartley</p>
      <p class="person__role">Chief Operating Officer</p>
    </div>
    <div class="divider"></div>
    <ul class="contacts">
      <li class="contacts__item">
        <svg class="contacts__icon" viewBox="0 0 16 16" aria-hidden="true"><path d="M1 5c0-2 3-3 7-3s7 1 7 3v1h-3V4.5C11 4 9.5 3.8 8 3.8S5 4 4 4.5V6H1z"/><path d="M3 7h10l1 7H2z"/></svg>
        <span>555-214-3080</span>
      </li>
      <li class="contacts__item">
        <svg class="contacts__icon" viewBox="0 0 16 16" aria-hidden="true"><rect x="4" y="1" width="8" height="4"/><rect x="1" y="6" width="14" height="6" rx="1"/><rect x="4" y="11" width="8" height="4"/></svg>
        <span>555-214-3082</span>
      </li>
      <li class="contacts__item">
        <svg class="contacts__icon" viewBox="0 0 16 16" aria-hidden="true"><path d="M1 3h14v10H1zM2.3 4.2v7.6h11.4V4.2L8 8.6z" fill-rule="evenodd"/></svg>
        <span>hello@northvalestudio.com</span>
      </li>
    </ul>
    <p class="address">48 Maple Court, Riverton, OH 44012</p>
  </section>

  <section class="card card--back">
    <div class="card__texture" role="img" aria-label="Dark charcoal low-poly faceted texture"></div>
    <div class="brand">
      <span class="brand__dot"></span>
      <span class="brand__name">Northvale Studio</span>
    </div>
    <p class="website">www.northvalestudio.com</p>
  </section>
</main>
</body>
</html>
```